TKR Fitters toolbox wrap design for mining

Hey guys, looking for something more stand out for my mining vehicles, I've attached photos of my current fleet at the moment, I am thinking to stick to the boxes only? I'm not convinced to go a car wrap on the body as we need to stick to a white vehicle. my current logo is red and black as pictured, I do have a second logo that incorporates a dark grey. I work on Blast hole drill rigs and Diggers (but mostly drills) TKR Fitters and services on Facebook. TKRfitters on instagram if you want to look at my profile (they're fairly new). i want to incorporate the call sign on the side and the rear as pictured, they do need to be same size for call sign but not same location.

I have on the vehicles bolvane toolbox 1280 long by 950 high and 616 deep, wanting the toolbox sides and rear of the boxes stickered

Have attached an example. And all my vehicles are Veltrana ranvors from 2018-2020 dual cabs. Tool box dimensions are 1280Lx616Dx950H.

Target Market(s)

Mining and machinery breakdowns

Industry/Entity Type

targetting breakdowns in heavy machinery mainly drills and diggers

Colors

Requirements
Must have
• would like to have colours like black red white greys, needs to have call sign in the design on the side and rear of toolbox
Nice to have
• silhouette of a drill rig and digger 452, 3700 or equivalent

```html
<!DOCTYPE html>
<html lang="en">
<head>
<meta charset="utf-8">
<title>TKR Fitters – Toolbox Wrap</title>
<link rel="stylesheet" href="https://fonts.googleapis.com/css2?family=Anton&display=swap">
<style>
  :root {
    --backdrop: #cbcbcb;
    --panel: #ffffff;
    --panel-top: #e0e1e1;
    --edge-top: #8990b0;
    --edge-bottom: #95a5b0;
    --rule: #c8c8c8;
    --brand-red: #bb0000;
    --brand-black: #000000;
    --steel: #80827f;
    --silhouette: #e2e2e2;
    --call-text: #ffffff;
  }
  html, body {
    margin: 0;
    padding: 0;
    width: 819px;
    height: 1200px;
    overflow: hidden;
    background: var(--backdrop);
  }
  .wrap-sheet {
    display: block;
    width: 819px;
    height: 1200px;
  }
  .section-label {
    font-family: "Anton", sans-serif;
    font-size: 76px;
    fill: var(--brand-black);
  }
  .panel-face { fill: var(--panel); }
  .panel-band { fill: var(--panel-top); }
  .panel-edge { fill: url(#edgeShade); }
  .text-rule { stroke: var(--rule); stroke-width: 4; }
  .call-badge { fill: var(--brand-red); }
  .call-sign {
    font-family: "Anton", sans-serif;
    fill: var(--call-text);
    text-anchor: middle;
  }
  .steel-accent { fill: var(--steel); }
  .silhouette { fill: var(--silhouette); }
  .brand-name {
    font-family: "Anton", sans-serif;
    font-size: 150px;
    fill: var(--brand-black);
  }
</style>
</head>
<body>
<svg class="wrap-sheet" viewBox="0 0 1586 2324" preserveAspectRatio="none" xmlns="http://www.w3.org/2000/svg">
  <defs>
    <linearGradient id="edgeShade" x1="0" y1="0" x2="0" y2="1">
      <stop offset="0" stop-color="#8990b0"/>
      <stop offset="1" stop-color="#95a5b0"/>
    </linearGradient>
  </defs>

  <!-- Rear panels -->
  <text class="section-label" x="44" y="156">BACK</text>

  <g class="rear-panel rear-panel--left">
    <polygon class="panel-edge" points="422,95 358,170 217,362 220,713 245,801 241,348"/>
    <polygon class="panel-face" points="422,95 682,95 686,795 245,801 241,348"/>
    <g class="text-rule">
      <line x1="474" y1="110" x2="671" y2="110"/>
      <line x1="462" y1="127" x2="671" y2="127"/>
      <line x1="449" y1="144" x2="671" y2="144"/>
      <line x1="437" y1="161" x2="671" y2="161"/>
      <line x1="424" y1="179" x2="671" y2="179"/>
      <line x1="412" y1="196" x2="671" y2="196"/>
      <line x1="399" y1="213" x2="671" y2="213"/>
      <line x1="387" y1="231" x2="671" y2="231"/>
      <line x1="374" y1="248" x2="671" y2="248"/>
      <line x1="362" y1="265" x2="671" y2="265"/>
      <line x1="255" y1="635" x2="453" y2="635"/>
      <line x1="255" y1="652" x2="465" y2="652"/>
      <line x1="255" y1="669" x2="478" y2="669"/>
      <line x1="255" y1="687" x2="490" y2="687"/>
      <line x1="255" y1="704" x2="503" y2="704"/>
      <line x1="255" y1="721" x2="515" y2="721"/>
      <line x1="255" y1="738" x2="528" y2="738"/>
      <line x1="255" y1="756" x2="540" y2="756"/>
      <line x1="255" y1="773" x2="553" y2="773"/>
      <line x1="255" y1="790" x2="565" y2="790"/>
    </g>
    <circle class="steel-accent" cx="349" cy="400" r="75" role="img" aria-label="Grey gear accent"/>
    <circle class="call-badge" cx="536" cy="468" r="128"/>
    <text class="call-sign" x="536" y="466" font-size="86">TKR</text>
    <text class="call-sign" x="536" y="560" font-size="96">04</text>
  </g>

  <g class="rear-panel rear-panel--right">
    <polygon class="panel-edge" points="1107,95 1172,170 1311,362 1309,713 1284,801 1288,348"/>
    <polygon class="panel-face" points="848,95 1107,95 1288,348 1284,801 843,795"/>
    <g class="text-rule">
      <line x1="857" y1="110" x2="1056" y2="110"/>
      <line x1="857" y1="127" x2="1068" y2="127"/>
      <line x1="857" y1="144" x2="1081" y2="144"/>
      <line x1="857" y1="161" x2="1093" y2="161"/>
      <line x1="857" y1="179" x2="1106" y2="179"/>
      <line x1="857" y1="196" x2="1118" y2="196"/>
      <line x1="857" y1="213" x2="1131" y2="213"/>
      <line x1="857" y1="231" x2="1143" y2="231"/>
      <line x1="857" y1="248" x2="1156" y2="248"/>
      <line x1="857" y1="265" x2="1167" y2="265"/>
      <line x1="1075" y1="635" x2="1273" y2="635"/>
      <line x1="1063" y1="652" x2="1273" y2="652"/>
      <line x1="1050" y1="669" x2="1273" y2="669"/>
      <line x1="1038" y1="687" x2="1273" y2="687"/>
      <line x1="1025" y1="704" x2="1273" y2="704"/>
      <line x1="1013" y1="721" x2="1273" y2="721"/>
      <line x1="1000" y1="738" x2="1273" y2="738"/>
      <line x1="988" y1="756" x2="1273" y2="756"/>
      <line x1="975" y1="773" x2="1273" y2="773"/>
      <line x1="963" y1="790" x2="1273" y2="790"/>
    </g>
    <circle class="steel-accent" cx="1180" cy="400" r="75" role="img" aria-label="Grey gear accent"/>
    <circle class="call-badge" cx="992" cy="468" r="128"/>
    <text class="call-sign" x="992" y="466" font-size="86">TKR</text>
    <text class="call-sign" x="992" y="560" font-size="96">04</text>
  </g>

  <!-- Side panels -->
  <text class="section-label" x="44" y="962">SIDES</text>

  <g class="side-panel side-panel--digger">
    <polygon class="panel-band" points="311,876 1256,878 1278,1112 287,1109"/>
    <polygon class="panel-face" points="287,1109 1278,1112 1277,1562 286,1558"/>
    <rect class="silhouette" x="305" y="1120" width="285" height="410" role="img" aria-label="Silhouette of a digger bucket and arm"/>
    <text class="brand-name" x="718" y="1048" textLength="490" lengthAdjust="spacingAndGlyphs">TKR Fitters</text>
    <g class="text-rule">
      <line x1="1075" y1="1390" x2="1273" y2="1390"/>
      <line x1="1063" y1="1407" x2="1273" y2="1407"/>
      <line x1="1050" y1="1424" x2="1273" y2="1424"/>
      <line x1="1038" y1="1442" x2="1273" y2="1442"/>
      <line x1="1025" y1="1459" x2="1273" y2="1459"/>
      <line x1="1013" y1="1476" x2="1273" y2="1476"/>
      <line x1="1000" y1="1493" x2="1273" y2="1493"/>
      <line x1="988" y1="1511" x2="1273" y2="1511"/>
      <line x1="975" y1="1528" x2="1273" y2="1528"/>
      <line x1="963" y1="1545" x2="1273" y2="1545"/>
    </g>
    <circle class="steel-accent" cx="1090" cy="1260" r="88" role="img" aria-label="Grey gear accent"/>
    <circle class="call-badge" cx="870" cy="1340" r="155"/>
    <text class="call-sign" x="870" y="1338" font-size="104">TKR</text>
    <text class="call-sign" x="870" y="1448" font-size="116">04</text>
  </g>

  <g class="side-panel side-panel--drill">
    <polygon class="panel-band" points="311,1600 1256,1602 1278,1836 287,1834"/>
    <polygon class="panel-face" points="287,1834 1278,1836 1277,2287 286,2283"/>
    <rect class="silhouette" x="438" y="1610" width="185" height="670" role="img" aria-label="Silhouette of a blast hole drill rig mast"/>
    <text class="brand-name" x="695" y="1772" textLength="490" lengthAdjust="spacingAndGlyphs">TKR Fitters</text>
    <g class="text-rule">
      <line x1="1052" y1="2122" x2="1250" y2="2122"/>
      <line x1="1040" y1="2139" x2="1250" y2="2139"/>
      <line x1="1027" y1="2156" x2="1250" y2="2156"/>
      <line x1="1015" y1="2174" x2="1250" y2="2174"/>
      <line x1="1002" y1="2191" x2="1250" y2="2191"/>
      <line x1="990" y1="2208" x2="1250" y2="2208"/>
      <line x1="977" y1="2225" x2="1250" y2="2225"/>
      <line x1="965" y1="2243" x2="1250" y2="2243"/>
      <line x1="952" y1="2260" x2="1250" y2="2260"/>
      <line x1="940" y1="2277" x2="1250" y2="2277"/>
    </g>
    <circle class="steel-accent" cx="1066" cy="1995" r="88" role="img" aria-label="Grey gear accent"/>
    <circle class="call-badge" cx="847" cy="2075" r="155"/>
    <text class="call-sign" x="847" y="2073" font-size="104">TKR</text>
    <text class="call-sign" x="847" y="2183" font-size="116">04</text>
  </g>
</svg>
</body>
</html>
```